FItness Bootcamp Flyer

We need an A4 flyer to distribute on an advertising board, and also distribute in the mail.

It should contain a photo(s) of females exercising and having fun outdoors.

It should contain the following text and if you think it could be worded better please change as I'm just looking at getting people to come along:

- KestrelMove Studio Outdoor Bootcamp
Get moving, get fit and feel great

Commencing 19th May

Get results before the winter season
6 Week Bootcamp for $49. Limited numbers!
Or casual visit $10 per session

Now is the time to:
- Lose Weight and Tone-up
- Build Strength and Endurance
- Increase Cardio Fitness
- Improve Your Energy and Vitality
- Fun Varied and Exciting Training Programs
- ALL Fitness Levels

LADIES ONLY BOOTCAMP SUBIACO
Monday 6:30-7:15am, 8:30-9:15am
Wednesday 6:30-7:!5am, 8:30-9:15am
Friday 8:30-9:15am,

Register you place now on 0428 574 812 or email: kestrelmovestudio@fernmail.net

flockpage.net/KestrelMove Studio

Target Market(s)

Females 20-60yrs

Industry/Entity Type

Advertising

Requirements
Nice to have
• - We like the words and style of the Harbourline Open Air Training flyer attached
- Also the Vanta Group brochure
- I like the colour Blue, Green, Pink. They don't all have to be used but at least one would be nice thank you

```html
<!DOCTYPE html>
<html lang="en">
<head>
<meta charset="utf-8">
<title>KestrelMove Studio Outdoor Bootcamp Flyer</title>
<link rel="stylesheet" href="https://fonts.googleapis.com/css2?family=Open+Sans:wght@400;600;700&family=Noto+Serif:ital,wght@1,700&display=swap">
<style>
  :root{
    --green:#8cc63f;
    --green-light:#c9e23c;
    --pink:#e8168a;
    --pink-dark:#c80f73;
    --blue:#29abe2;
    --rule-blue:#1f6fb8;
    --navy:#1d2b6e;
    --white:#ffffff;
    --grey:#d6d6d6;
    --page:#ececec;
  }
  *{box-sizing:border-box;margin:0;padding:0}
  html,body{width:1040px;height:1200px;overflow:hidden;background:var(--page)}
  .flyer{position:absolute;left:105px;top:30px;width:830px;height:1140px;background:var(--white);overflow:hidden;font-family:"Open Sans",sans-serif;color:var(--white)}
  .photo{position:absolute;left:0;top:110px;width:830px;height:508px;background:linear-gradient(180deg,#eef6fb 0%,#cfe4ef 35%,#a9c3a0 62%,#5f7d45 82%,#4a5f35 100%)}
  .header-curve{position:absolute;left:0;top:0;width:830px;height:240px}
  .brand-title{position:absolute;left:0;top:24px;width:830px;text-align:center;font-family:"Noto Serif",serif;font-style:italic;font-weight:700;font-size:63px;line-height:1.1;color:var(--white);text-shadow:2px 3px 4px rgba(0,0,0,.35)}
  .headline{position:absolute;left:0;width:830px;text-align:center;font-weight:700;color:var(--pink);letter-spacing:-.5px;
    text-shadow:-2px -2px 0 #fff,2px -2px 0 #fff,-2px 2px 0 #fff,2px 2px 0 #fff,0 2px 0 #fff,0 -2px 0 #fff,2px 0 0 #fff,-2px 0 0 #fff,2px 4px 6px rgba(0,0,0,.35)}
  .headline.date{top:426px;font-size:58px}
  .headline.name{top:504px;font-size:35px}
  .headline.tagline{top:554px;font-size:35px}
  .benefits{position:absolute;left:0;top:618px;width:830px;height:142px;background:var(--green)}
  .benefits-intro{position:absolute;left:38px;top:10px;font-size:20px;font-weight:600}
  .benefit-list{position:absolute;top:38px;list-style:none}
  .benefit-list.left{left:24px}
  .benefit-list.right{left:364px}
  .benefit-list li{display:flex;align-items:center;height:27px;font-size:20px;font-weight:600;white-space:nowrap}
  .benefit-list svg{width:16px;height:16px;margin-right:8px;flex:none}
  .rule{position:absolute;left:0;width:830px;height:6px;background:var(--rule-blue)}
  .rule.top{top:760px}
  .rule.bottom{top:1040px}
  .schedule-title{position:absolute;left:23px;top:806px;font-family:"Noto Serif",serif;font-style:italic;font-weight:700;font-size:24px;color:var(--navy)}
  .schedule{position:absolute;left:19px;top:852px;width:437px;height:160px;display:flex;border-radius:6px;overflow:hidden;border-top:6px solid var(--pink)}
  .day{flex:1;display:flex;flex-direction:column;justify-content:center;align-items:center;font-size:19px;line-height:1.35;text-align:center}
  .day .day-name{font-weight:600}
  .day.monday{background:var(--pink)}
  .day.wednesday{background:var(--green)}
  .day.friday{background:var(--blue);margin-top:6px;border-top-left-radius:4px}
  .offer{position:absolute;left:462px;top:748px;width:368px;height:290px}
  .offer svg{position:absolute;left:0;top:0}
  .offer-text{position:absolute;left:0;top:20px;width:368px;text-align:center;font-size:21px;line-height:1.4}
  .offer-text .lead{font-size:21px;line-height:1.38;margin-bottom:8px}
  .offer-text strong{font-weight:700;font-size:26px}
  .offer-text p{margin:0}
  .footer{position:absolute;left:0;top:1046px;width:830px;height:94px;background:var(--green)}
  .register{position:absolute;left:0;top:8px;width:830px;text-align:center;font-size:18.5px}
  .register strong{font-weight:700}
  .social{position:absolute;left:0;top:41px;width:830px;display:flex;justify-content:center;align-items:center;font-size:20px;font-weight:600}
  .social .mark{width:30px;height:30px;background:var(--navy);margin-right:18px}
</style>
</head>
<body>
<main class="flyer">
  <div class="photo" role="img" aria-label="Photo of four women laughing and stretching together outdoors on a sunny hillside trail"></div>
  <svg class="header-curve" viewBox="0 0 830 240" aria-hidden="true">
    <defs>
      <radialGradient id="headerGlow" cx="0.6" cy="0.15" r="0.7">
        <stop offset="0" stop-color="#c9e23c"/>
        <stop offset="0.6" stop-color="#8cc63f"/>
      </radialGradient>
    </defs>
    <path d="M0 0H830V211C780 150 680 120 460 118C250 117 100 125 0 137Z" fill="url(#headerGlow)"/>
  </svg>
  <h1 class="brand-title">KestrelMove Studio</h1>

  <p class="headline date">Commencing 19th May</p>
  <p class="headline name">KestrelMove Studio Outdoor Bootcamp</p>
  <p class="headline tagline">Get moving, get fit and feel great</p>

  <section class="benefits">
    <p class="benefits-intro">Now is the time to:</p>
    <ul class="benefit-list left">
      <li><svg viewBox="0 0 16 16"><path d="M5 3l6 5-6 5" fill="none" stroke="#fff" stroke-width="2.5"/></svg>Lose Weight and Tone-up</li>
      <li><svg viewBox="0 0 16 16"><path d="M5 3l6 5-6 5" fill="none" stroke="#fff" stroke-width="2.5"/></svg>Build Strength and Endurance</li>
      <li><svg viewBox="0 0 16 16"><path d="M5 3l6 5-6 5" fill="none" stroke="#fff" stroke-width="2.5"/></svg>Increase Cardio Fitness</li>
    </ul>
    <ul class="benefit-list right">
      <li><svg viewBox="0 0 16 16"><path d="M5 3l6 5-6 5" fill="none" stroke="#fff" stroke-width="2.5"/></svg>Improve Your Energy and Vitality</li>
      <li><svg viewBox="0 0 16 16"><path d="M5 3l6 5-6 5" fill="none" stroke="#fff" stroke-width="2.5"/></svg>Fun Varied and Exciting Training Programs</li>
      <li><svg viewBox="0 0 16 16"><path d="M5 3l6 5-6 5" fill="none" stroke="#fff" stroke-width="2.5"/></svg>ALL Fitness Levels</li>
    </ul>
  </section>

  <div class="rule top"></div>

  <h2 class="schedule-title">LADIES ONLY BOOTCAMP SUBIACO</h2>
  <div class="schedule">
    <div class="day monday"><span class="day-name">Monday</span><span>6:30-7:15am</span><span>8:30-9:15am</span></div>
    <div class="day wednesday"><span class="day-name">Wednesday</span><span>6:30-7:15am</span><span>8:30-9:15am</span></div>
    <div class="day friday"><span class="day-name">Friday</span><span>8:30-9:15am</span></div>
  </div>

  <aside class="offer">
    <svg width="368" height="290" viewBox="0 0 368 290" aria-hidden="true">
      <defs>
        <linearGradient id="offerPink" x1="0" y1="0" x2="0" y2="1">
          <stop offset="0" stop-color="#ef3c9c"/>
          <stop offset="1" stop-color="#e8168a"/>
        </linearGradient>
      </defs>
      <polygon points="64,2 286,2 368,144 286,286 64,286 0,144" fill="#d6d6d6"/>
      <polygon points="74,16 276,16 350,144 276,272 74,272 16,144" fill="url(#offerPink)"/>
      <polygon points="88,250 262,250 254,282 96,282" fill="#c80f73"/>
    </svg>
    <div class="offer-text">
      <div class="lead">Get results<br>before the winter<br>season</div>
      <p><strong>6 Week</strong> Bootcamp for</p>
      <p><strong>$49</strong>. Limited numbers!</p>
      <p>Or casual visit <strong>$10</strong></p>
      <p>per session</p>
    </div>
  </aside>

  <div class="rule bottom"></div>

  <footer class="footer">
    <p class="register">Register you place now on <strong>0428 574 812</strong> | email: <strong>kestrelmovestudio@fernmail.net</strong></p>
    <p class="social"><span class="mark"></span>flockpage.net/KestrelMove Studio</p>
  </footer>
</main>
</body>
</html>
```